Seed Company Looking For a Soybean Seed Bag Design

We are are a regional seed company who is currently launching a new line of soybean products. The brand of the product will be Tru-Crop. We are looking for a custom design of a soybean bag measuring 16"x5"x30" (when constructed). We are looking for a modern design that's relatively loud, but not too busy. The proof needs to match with the attached template. We have also provided a proof of a previous bag project (Fox-Ridge-Standard) we've done to show how the artwork needs to be laid out. In no way does the new design need to resemble the example. Also attached are some other examples of seed bags.
Industry/Entity Type
Agriculture
Colors
Designer to choose colors to be used in the design.
Look and feel
Each slider illustrates characteristics of the customer's brand and the style your logo design should communicate.

```html
<!DOCTYPE html>
<html lang="en">
<head>
<meta charset="UTF-8">
<title>Tru-Crop Soybean Seeds – Bag Front</title>
<link rel="stylesheet" href="https://fonts.googleapis.com/css2?family=Antonio:wght@600;700&family=Kaushan+Script&display=swap">
<style>
  :root {
    --backdrop: #3ee577;
    --bag-white: #f4f4f4;
    --bag-green: #1fd061;
    --ink: #111111;
    --leaf-green: #157a2e;
    --soy-light: #d9a95c;
    --soy-dark: #b88440;
  }
  html, body {
    margin: 0;
    padding: 0;
    width: 1200px;
    height: 803px;
    overflow: hidden;
    background: var(--backdrop);
  }
  .canvas {
    position: relative;
    width: 1200px;
    height: 803px;
  }
  .bag-front {
    position: absolute;
    left: 0;
    top: 0;
    width: 1200px;
    height: 803px;
  }
  .brand-name {
    font-family: "Antonio", sans-serif;
    font-weight: 700;
    fill: var(--ink);
  }
  .product-title {
    font-family: "Antonio", sans-serif;
    font-weight: 700;
    fill: var(--ink);
  }
  .product-subtitle {
    font-family: "Kaushan Script", cursive;
    fill: var(--leaf-green);
  }
  .bag-white { fill: var(--bag-white); }
  .bag-green { fill: var(--bag-green); }
  .brand-mark { fill: var(--ink); }
</style>
</head>
<body>
<main class="canvas">
  <svg class="bag-front" viewBox="0 0 1200 803" xmlns="http://www.w3.org/2000/svg">
    <defs>
      <radialGradient id="soy-fill" cx="50%" cy="50%" r="70%">
        <stop offset="0%" stop-color="var(--soy-light)"/>
        <stop offset="100%" stop-color="var(--soy-dark)"/>
      </radialGradient>
    </defs>

    <!-- Upper white panel -->
    <rect class="bag-white" x="456" y="105" width="297" height="336"/>
    <!-- Lower green panel -->
    <rect class="bag-green" x="456" y="441" width="297" height="261"/>

    <!-- Brand -->
    <g class="brand">
      <rect class="brand-mark" x="563" y="163" width="12" height="12"/>
      <text class="brand-name" x="580" y="176" font-size="20">Tru-Crop</text>
    </g>

    <!-- Product name -->
    <text class="product-title" x="477" y="352" font-size="112" textLength="252" lengthAdjust="spacingAndGlyphs">SOYBEAN</text>
    <text class="product-subtitle" x="477" y="410" font-size="88" textLength="249" lengthAdjust="spacingAndGlyphs">seeds</text>

    <!-- Soybean photo area -->
    <rect class="soy-photo" role="img" aria-label="Two bean-shaped windows showing a close-up photo of dried soybeans"
          x="465" y="453" width="267" height="228" rx="24" fill="url(#soy-fill)"/>
  </svg>
</main>
</body>
</html>
```